Logo and Business Card for Dental Office

We are opening a periodontal office (dental specialist for dental implants and gum diseases). It is a brand new state of the art facility with a focus on the most effective treatments for retaining natural teeth, or replacing teeth with implants when they must be lost. Strong emphasis on customer service and amenities for patient comfort. We are located just outside of Boston, MA.

Target Market(s)

potential adult patients, dentists in the community that will refer patients for specialized care

Industry/Entity Type

Dental

Requirements
Must have
• business name, address, phone number, website
Marcus T. Pellinger, DMD LLC
427 Corliss Street, Ste 305
Elmsford Glen, VT 05999
555-201-0172
555-201-0148 Fax
DrPellinger.example

the uploaded file has a rough version of what I'm looking for in the logo, I like the colors but it can be varies some.
Nice to have
• simple logo or symbol on business card, one possible idea I had was an abstract symbol of a screw or threads that might represent a dental implant, the attached file gives an idea of where to start.
Should not have
• I want a professional feel, no cartoons of teeth that appear childish, etc
The font should be easy to read with no curly/swirly shapes.

```html
<!DOCTYPE html>
<html lang="en">
<head>
<meta charset="utf-8">
<title>Periodontics &amp; Dental Implants – Business Card</title>
<link rel="stylesheet" href="https://fonts.googleapis.com/css2?family=Questrial&display=swap">
<style>
  :root {
    --page: #e6e6e6;
    --card-white: #ffffff;
    --brand-red: #74241f;
    --accent-red: #a51c1c;
    --ink: #2a2a2a;
    --ink-soft: #4a4a4a;
    --on-red: #ffffff;
  }
  * { box-sizing: border-box; margin: 0; padding: 0; }
  html, body {
    width: 1200px; height: 857px; overflow: hidden;
    background: var(--page);
    font-family: "Questrial", Arial, sans-serif;
  }
  .sheet {
    position: relative; width: 1200px; height: 857px;
    display: flex; align-items: center; justify-content: center; gap: 60px;
  }
  .card {
    position: relative; width: 520px; height: 297px;
    box-shadow: 0 6px 18px rgba(0,0,0,.18);
  }
  .card--front { background: var(--card-white); color: var(--ink); }
  .card--back { background: var(--brand-red); color: var(--on-red);
    display: flex; align-items: center; justify-content: center; }

  .wordmark { display: flex; align-items: center; gap: 10px; }
  .wordmark__square { width: 12px; height: 12px; background: var(--accent-red); flex: none; }
  .wordmark__name { font-size: 21px; line-height: 1.1; color: var(--ink); white-space: nowrap; }
  .card--front .wordmark { position: absolute; left: 40px; top: 40px; }

  .contact { position: absolute; left: 40px; top: 146px; }
  .contact__name { font-size: 17px; letter-spacing: .3px; color: var(--ink); }
  .contact__cred { font-size: 9px; color: var(--accent-red); margin-left: 4px; vertical-align: 3px; }
  .contact__address { margin-top: 12px; font-size: 10.5px; line-height: 1.3; color: var(--ink-soft); }
  .contact__lines { margin-top: 5px; font-size: 8px; color: var(--ink-soft); }
  .contact__lines b { font-weight: normal; color: var(--accent-red); }
  .contact__lines span + span { margin-left: 8px; }
  .contact__email { margin-top: 3px; font-size: 10.5px; color: var(--ink-soft); }
  .contact__email b { font-weight: normal; color: var(--accent-red); }
  .contact__web { margin-top: 6px; font-size: 16px; letter-spacing: .6px; color: var(--brand-red); }

  .back-mark { text-align: center; }
  .back-mark .wordmark { justify-content: center; }
  .back-mark .wordmark__square { background: var(--on-red); }
  .back-mark .wordmark__name { color: var(--on-red); font-size: 25px; }
  .back-mark__owner { margin-top: 8px; font-size: 10px; letter-spacing: 1px; text-transform: uppercase; }
</style>
</head>
<body>
<main class="sheet">
  <section class="card card--front" aria-label="Business card front">
    <div class="wordmark">
      <span class="wordmark__square"></span>
      <span class="wordmark__name">Periodontics &amp; Dental Implants</span>
    </div>
    <div class="contact">
      <p class="contact__name">Marcus T. Pellinger<span class="contact__cred">DMD LLC</span></p>
      <p class="contact__address">427 Corliss Street, Ste 305<br>Elmsford Glen, VT 05999</p>
      <p class="contact__lines"><span><b>t:</b> 555-201-0172</span><span><b>f:</b> 555-201-0148</span></p>
      <p class="contact__email"><b>e:</b> mpellinger@example.com</p>
      <p class="contact__web">www.DrPellinger.example</p>
    </div>
  </section>

  <section class="card card--back" aria-label="Business card back">
    <div class="back-mark">
      <div class="wordmark">
        <span class="wordmark__square"></span>
        <span class="wordmark__name">Periodontics &amp; Dental Implants</span>
      </div>
      <p class="back-mark__owner">Marcus T. Pellinger DMD, LLC</p>
    </div>
  </section>
</main>
</body>
</html>
```